Wine business webpage
Italian fine wines
Project: Wine business webpage
Wine business webpage -
Creative Brief
Fine and Rare Italian wine merchant
Cantina del Sole specializes in the Italy's fine and rare wines. We have special relationships with many of the greatest estates and their distributors, and are able to pass on the benefits of those relationships to our customers. We would welcome the opportunity to put our passion and knowledge to work for you!
Dislike: homepage with loads of bottles of wine, e.g. http://www.vintageharborcellars.example/
Nature
natural wood
green - Terre Verte
earth tone
top
http://www.marlowecask.example/
http://www.grapeledgerhub.example/
http://www.vinoquay.example/

```html
<!DOCTYPE html>
<html lang="en">
<head>
<meta charset="utf-8">
<title>Cantina del Sole — Fine and Rare Italian Wines</title>
<link href="https://fonts.googleapis.com/css2?family=Cinzel:wght@500&family=Great+Vibes&family=Open+Sans:wght@400;600&family=Cormorant+Garamond:wght@500&display=swap" rel="stylesheet">
<style>
  :root {
    --wood-dark: #2a1a10;
    --wood-mid: #4a2f1c;
    --wood-light: #6b4529;
    --cream: #efe3cc;
    --cream-deep: #e2cfae;
    --nav-brown: #8a5a3a;
    --band-brown: #a46f4a;
    --terre-verte: #6f7a44;
    --terre-verte-dark: #3e4426;
    --wine-red: #6d1220;
    --ink: #3a2a1e;
    --muted: #6d5a48;
    --strip-dark: #24201d;
    --white: #fbf6ec;
  }
  * { box-sizing: border-box; margin: 0; padding: 0; }
  html, body { width: 1200px; height: 1072px; overflow: hidden; }
  body {
    position: relative;
    font-family: "Open Sans", Arial, sans-serif;
    color: var(--ink);
    background:
      repeating-linear-gradient(90deg, rgba(0,0,0,.18) 0 2px, transparent 2px 170px),
      linear-gradient(180deg, var(--wood-light) 0%, var(--wood-mid) 45%, var(--wood-dark) 100%);
  }
  .abs { position: absolute; }

  /* header */
  .brand { left: 200px; top: 34px; width: 170px; text-align: center; }
  .brand-mark { width: 46px; height: 46px; border: 2px solid var(--cream); border-radius: 50%; margin: 0 auto 8px; }
  .brand-name { font-family: "Cinzel", serif; font-size: 24px; color: var(--cream); letter-spacing: 1px; line-height: 1; }
  .search { left: 826px; top: 106px; display: flex; gap: 6px; align-items: center; }
  .search-label { font-size: 10px; color: var(--cream); background: #1b120c; padding: 2px 5px; }
  .search-field { width: 120px; height: 18px; background: var(--white); font-size: 10px; padding: 2px 6px; color: var(--muted); }
  .main-nav { left: 390px; top: 146px; width: 625px; height: 30px; background: var(--nav-brown); display: flex; justify-content: space-around; align-items: center; }
  .main-nav a { color: var(--white); text-decoration: none; font-size: 15px; }

  /* page panel */
  .page { left: 145px; top: 180px; width: 913px; height: 756px; background: linear-gradient(180deg, var(--cream) 0%, var(--cream-deep) 100%); box-shadow: 0 0 18px rgba(0,0,0,.5); }
  .hero-photo { left: 203px; top: 209px; width: 194px; height: 284px; background: radial-gradient(circle at 60% 40%, #a8323b 0%, var(--wine-red) 40%, #1a0b08 100%); }
  .hero-banner { left: 415px; top: 209px; width: 591px; height: 284px; background: radial-gradient(circle at 35% 55%, #8b955a 0%, var(--terre-verte) 45%, var(--terre-verte-dark) 100%); }
  .hero-title { left: 440px; top: 385px; font-family: "Cinzel", serif; font-size: 38px; color: var(--white); }
  .hero-copy { left: 755px; top: 240px; width: 230px; font-size: 10px; line-height: 1.5; color: var(--white); }
  .hero-copy p + p { margin-top: 8px; }

  /* sidebar */
  .sidebar { left: 209px; top: 528px; width: 119px; height: 377px; background: var(--cream-deep); border: 1px solid #c9ad86; padding: 8px; }
  .sidebar-title { background: var(--band-brown); color: var(--white); font-size: 9px; text-align: center; padding: 4px 0; margin-bottom: 12px; text-transform: uppercase; }
  .category-list { list-style: none; font-size: 10px; line-height: 1.7; padding-left: 12px; }
  .category-list li::before { content: "▸ "; color: var(--wine-red); }
  .side-button { margin-top: 12px; background: var(--band-brown); color: var(--white); font-size: 9px; text-align: center; padding: 5px 0; }
  .subscribe { margin-top: 18px; text-align: center; }
  .subscribe-title { font-family: "Cormorant Garamond", serif; font-size: 17px; color: var(--wine-red); letter-spacing: 1px; }
  .subscribe-field { height: 16px; background: var(--white); border: 1px solid #c9ad86; margin-top: 6px; }

  /* welcome */
  .welcome { left: 348px; top: 528px; width: 652px; height: 168px; background: linear-gradient(180deg, var(--cream) 0%, #e6c9a4 100%); padding: 12px 20px; }
  .welcome h1 { font-family: "Great Vibes", cursive; font-weight: 400; font-size: 30px; color: var(--ink); margin-left: 70px; }
  .welcome-cols { display: flex; gap: 40px; margin-top: 8px; font-size: 10px; line-height: 1.5; color: var(--muted); }
  .welcome-cols p + p { margin-top: 8px; }

  /* feature strip */
  .feature-strip { left: 348px; top: 705px; width: 652px; height: 136px; background: var(--strip-dark); display: flex; gap: 10px; padding: 12px; }
  .feature { flex: 1; border: 1px solid #3e3631; display: flex; align-items: center; justify-content: space-between; padding: 0 14px; color: var(--cream); font-size: 11px; }
  .feature-arrow { color: var(--band-brown); font-size: 16px; }
  .feature-photo { flex: 0 0 180px; background: linear-gradient(135deg, #7a1a22 0%, #3b2a22 50%, #c9b89a 100%); }

  /* quote band */
  .quote-band { left: 348px; top: 870px; width: 652px; height: 52px; background: #e2c9a5; border: 1px solid #c9ad86; display: flex; justify-content: space-between; align-items: center; padding: 0 24px; font-size: 10px; color: var(--muted); }
  .quote-band p { width: 280px; text-align: center; }

  .bottom-band { left: 116px; top: 935px; width: 972px; height: 31px; background: var(--band-brown); }
  .social { left: 740px; top: 922px; width: 246px; height: 53px; background: var(--cream); box-shadow: 0 2px 6px rgba(0,0,0,.4); display: flex; justify-content: center; align-items: center; gap: 12px; }
  .social-square { width: 24px; height: 24px; background: var(--band-brown); }
  .footer-note { left: 160px; top: 1000px; width: 320px; font-size: 10px; line-height: 1.5; color: #a58a70; }
</style>
</head>
<body>
  <header>
    <div class="brand abs">
      <div class="brand-mark"></div>
      <div class="brand-name">Cantina del Sole</div>
    </div>
    <div class="search abs"><span class="search-label">Go</span><span class="search-field">Search</span></div>
    <nav class="main-nav abs">
      <a href="#">Home</a><a href="#">About Us</a><a href="#">Our Wines</a><a href="#">Ordering</a><a href="#">News</a><a href="#">Contact Us</a>
    </nav>
  </header>

  <main>
    <div class="page abs"></div>
    <div class="hero-photo abs" role="img" aria-label="Glass of red wine poured in a warm cellar"></div>
    <div class="hero-banner abs" role="img" aria-label="Green damask backdrop for the welcome banner"></div>
    <div class="hero-title abs">Cantina del Sole</div>
    <div class="hero-copy abs">
      <p>Fine estate wines from across Italy, chosen with care and sent to your door. Our cellar holds rare vintages from trusted growers.</p>
      <p>Ask our team for advice on any bottle or region.</p>
    </div>

    <aside class="sidebar abs">
      <div class="sidebar-title">Our Categories</div>
      <ul class="category-list">
        <li>AUSTRALIAN</li><li>BORDEAUX</li><li>BURGUNDY</li><li>CABERNET</li><li>CHAMPAGNE</li><li>CHARDONNAY</li><li>ITALIAN</li><li>MERLOT</li><li>OTHER</li>
      </ul>
      <div class="side-button">Wine Tasting Club</div>
      <div class="side-button">Gift Vouchers</div>
      <div class="subscribe">
        <div class="subscribe-title">SUBSCRIBE</div>
        <div class="subscribe-field"></div>
      </div>
    </aside>

    <section class="welcome abs">
      <h1>Welcome</h1>
      <div class="welcome-cols">
        <div>
          <p>We work closely with great Italian estates and pass the benefit on to you. Every wine is tasted and stored with care.</p>
          <p>Browse our list by region or grape and order online in minutes.</p>
        </div>
        <div>
          <p>From Barolo to Brunello, our buyers seek out small producers and rare vintages worth keeping.</p>
          <p>Join our list to hear about new releases first.</p>
        </div>
      </div>
    </section>

    <section class="feature-strip abs">
      <div class="feature"><span class="feature-arrow">‹</span><span>New Arrivals</span><span class="feature-arrow">›</span></div>
      <div class="feature"><span class="feature-arrow">‹</span><span>Top Picks</span><span class="feature-arrow">›</span></div>
      <div class="feature-photo" role="img" aria-label="Rack of wine bottles with red capsules"></div>
    </section>

    <section class="quote-band abs">
      <p>Passion and knowledge put to work for every order we send.</p>
      <p>Special terms for trade buyers and private cellars alike.</p>
    </section>
  </main>

  <footer>
    <div class="bottom-band abs"></div>
    <div class="social abs">
      <span class="social-square"></span><span class="social-square"></span><span class="social-square"></span><span class="social-square"></span><span class="social-square"></span><span class="social-square"></span>
    </div>
    <p class="footer-note abs">Copyright 2024 Cantina del Sole. All rights reserved. Fine and rare Italian wines.</p>
  </footer>
</body>
</html>
```